Borealis Trailworks Therapy needs Corporate Team Building Brochure

Borealis Trailworks Therapy is a new company in Vancouver Canada. We do adventure based counselling, family counselling, groups and team building events. We are looking to expand our marketing to the corporate team building world. What makes us different is that we don't just take people to play games and do adventure activities, we are able to use our training in psychology and coaching to make more of an impact. We would like to see designs that are professional and engaging, something that shows our wild adventure side. Our website is being redone, but to get a sense check out www.borealistrailworks-example.com

Target Market(s)

Vancouver downtown corporate teams.

Industry/Entity Type

Building

Font styles to use
Serif

Colors
acd037

Requirements
Must have
• some reference (visual or otherwise) to adventure activities, we do rock climbing, sea kayaking, hiking, as well as team building challenge initiatives.
• This is a flyer specifically for our team building services, it is not a general borealis trailworks therapy flyer. Use name Borealis Trailworks, not Borealis Trailworks Therapy

```html
<!DOCTYPE html>
<html lang="en">
<head>
<meta charset="utf-8">
<title>Borealis Trailworks – Corporate Team Building Brochure</title>
<link href="https://fonts.googleapis.com/css2?family=Montserrat:ital,wght@0,600;0,700;0,800;1,700;1,800&family=Open+Sans:wght@400;600;700&display=swap" rel="stylesheet">
<style>
:root{
  --green:#3f9a2c;
  --green-dark:#2d7a1f;
  --lime:#acd037;
  --ink:#2b2b2b;
  --muted:#555;
  --paper:#ffffff;
  --backdrop:#e9ebe6;
}
*{box-sizing:border-box;margin:0;padding:0}
html,body{width:847px;height:1200px;overflow:hidden}
body{background:var(--backdrop);font-family:"Open Sans",Arial,sans-serif;color:var(--ink);position:relative}
.sheet{position:absolute;left:20px;width:807px;height:540px;background:var(--paper);display:flex;box-shadow:0 4px 14px rgba(0,0,0,.18)}
.sheet--outside{top:40px}
.sheet--inside{top:620px}
.panel{width:269px;height:100%;position:relative;overflow:hidden;display:flex;flex-direction:column}
.panel + .panel{border-left:1px solid #e4e4e4}
.photo{width:100%;flex:none}
.heading{font-family:"Montserrat",Arial,sans-serif;font-weight:800;text-transform:uppercase;letter-spacing:.5px}
.body-text{font-size:8.6px;line-height:1.5;color:var(--muted)}
.body-text p+p{margin-top:6px}
.green-strong{color:var(--green);font-weight:700}
.brand{display:flex;align-items:center;gap:7px;font-family:"Montserrat",Arial,sans-serif;font-weight:700;font-size:15px;color:var(--green)}
.brand-dot{width:22px;height:22px;border-radius:50%;background:var(--lime);flex:none}

/* outside sheet */
.about .photo{height:190px;background:linear-gradient(160deg,#7fb2c9 0%,#3e7d8f 55%,#d24c3a 100%)}
.about .content{padding:16px 18px}
.about .heading{font-size:15px;color:var(--green);margin-bottom:8px}
.testimonials{background:var(--green);color:#fff}
.testimonials .upper{padding:20px 18px 14px}
.testimonials .heading{font-size:15px;text-align:center;margin-bottom:10px}
.quote{font-size:9px;line-height:1.55;font-style:italic;text-align:center}
.quote-author{margin-top:8px;text-align:right;font-size:9px;font-style:italic;font-weight:600}
.contact{margin-top:auto;background:#fff;color:var(--ink);padding:18px 18px 22px;display:flex;flex-direction:column;align-items:center;gap:8px}
.contact .phone{display:flex;align-items:center;gap:6px;font-family:"Montserrat",Arial,sans-serif;font-weight:800;font-size:19px;color:var(--green)}
.contact .line{font-size:9px;color:var(--muted)}
.cover .brand-bar{padding:16px 16px 12px}
.cover .photo{height:290px;background:linear-gradient(180deg,#b9c9d6 0%,#7f97a8 45%,#4a5a3f 100%)}
.tagline{background:var(--green);color:#fff;flex:1;display:flex;flex-direction:column;justify-content:center;align-items:center;text-align:center;font-family:"Montserrat",Arial,sans-serif;font-style:italic;text-transform:uppercase;line-height:1.15}
.tagline .small{font-size:13px;font-weight:700}
.tagline .big{font-size:22px;font-weight:800}

/* inside sheet */
.teams .content{padding:18px 18px 10px}
.teams .heading,.retreat .heading{font-size:15px;color:var(--green);margin-bottom:8px}
.sub{font-family:"Montserrat",Arial,sans-serif;font-weight:700;font-size:10.5px;color:var(--green);margin-bottom:5px}
.more{font-family:"Montserrat",Arial,sans-serif;font-weight:800;text-transform:uppercase;color:var(--green);text-align:center;font-size:17px;line-height:1.15;padding:8px 10px}
.teams .photo{margin-top:auto;height:150px;background:linear-gradient(180deg,#c9e08a 0%,#7fae3a 60%,#2f5a1c 100%)}
.leadership .photo{height:180px;background:linear-gradient(170deg,#d6c9a6 0%,#8aa86b 50%,#3f6b2c 100%)}
.leadership .band{background:var(--green);color:#fff;padding:10px 18px}
.leadership .band .heading{font-size:15px}
.leadership .content{padding:12px 18px}
.retreat .content{padding:18px 18px 0}
.activities-title{font-family:"Montserrat",Arial,sans-serif;font-weight:800;font-size:11px;color:var(--green);margin:8px 0 4px;text-transform:uppercase}
.activities{display:grid;grid-template-columns:1fr 1fr;gap:2px 8px;list-style:none;font-size:8.5px;color:var(--muted)}
.activities li{display:flex;gap:4px;align-items:flex-start}
.activities svg{flex:none;margin-top:2px}
.dates{background:var(--green);margin:10px 0 0;padding:8px 12px;color:#fff;text-align:center}
.dates .label{font-family:"Montserrat",Arial,sans-serif;font-weight:800;font-size:11px;text-transform:uppercase;margin-bottom:6px}
.date-pills{display:flex;gap:8px;justify-content:center}
.pill{background:#fff;color:var(--green);font-weight:700;font-size:8.5px;padding:3px 8px;border-radius:3px}
.retreat .lower{position:relative;flex:1;background:linear-gradient(180deg,#d7e8f0 0%,#95b8c7 100%)}
.location{position:relative;padding:8px 18px 0;width:60%}
.price{position:absolute;right:14px;bottom:14px;width:92px;height:92px;border-radius:50%;background:var(--green);border:3px solid #fff;color:#fff;display:flex;flex-direction:column;align-items:center;justify-content:center;font-family:"Montserrat",Arial,sans-serif;text-align:center}
.price .amount{font-size:30px;font-weight:800;line-height:1}
.price .per{font-size:8px;font-weight:700;text-transform:uppercase;line-height:1.2}
</style>
</head>
<body>

<section class="sheet sheet--outside">
  <article class="panel about">
    <div class="photo" role="img" aria-label="Photograph of a sea kayaker paddling through whitewater"></div>
    <div class="content">
      <h2 class="heading">About Us</h2>
      <div class="body-text">
        <p>Borealis Trailworks brings downtown Vancouver teams into the wild for team building that goes deeper than games. Our facilitators are trained in psychology and coaching.</p>
        <p>We guide your team through rock climbing, sea kayaking, hiking and challenge initiatives, then help everyone reflect on how they communicate, lead and trust one another.</p>
        <p><span class="green-strong">Adventure with real impact</span> means your team returns to the office with shared insight, stronger working relationships and clear next steps.</p>
      </div>
    </div>
  </article>

  <article class="panel testimonials">
    <div class="upper">
      <h2 class="heading">Testimonials</h2>
      <p class="quote">“Our team has done plenty of outings, but this was different. The climbing day was a blast, and the debrief afterwards changed how we run meetings. We still use the tools the facilitators gave us months later.”</p>
      <p class="quote-author">– Dana Whitlow</p>
    </div>
    <div class="contact">
      <div class="brand"><span class="brand-dot"></span>Borealis Trailworks</div>
      <div class="phone">
        <svg width="16" height="16" viewBox="0 0 24 24" aria-hidden="true"><path fill="currentColor" d="M6.6 10.8a15.1 15.1 0 0 0 6.6 6.6l2.2-2.2a1 1 0 0 1 1-.25 11.4 11.4 0 0 0 3.6.57 1 1 0 0 1 1 1V20a1 1 0 0 1-1 1A17 17 0 0 1 3 4a1 1 0 0 1 1-1h3.5a1 1 0 0 1 1 1c0 1.25.2 2.45.57 3.57a1 1 0 0 1-.25 1z"/></svg>
        (604) 555-0142
      </div>
      <div class="line">info@borealistrailworks-example.com</div>
      <div class="line">www.borealistrailworks-example.com</div>
    </div>
  </article>

  <article class="panel cover">
    <div class="brand-bar"><div class="brand"><span class="brand-dot"></span>Borealis Trailworks</div></div>
    <div class="photo" role="img" aria-label="Photograph of a team hiking across a snowy mountain ridge"></div>
    <div class="tagline">
      <span class="small">Building</span>
      <span class="big">Stronger Teams</span>
      <span class="small">Through</span>
      <span class="big">Adventure</span>
    </div>
  </article>
</section>

<section class="sheet sheet--inside">
  <article class="panel teams">
    <div class="content">
      <h2 class="heading">Team Programs</h2>
      <h3 class="sub">Climbing for Communication</h3>
      <div class="body-text">
        <p>A half or full day on the rock where colleagues belay, coach and encourage each other. Every climb depends on clear communication and trust.</p>
        <p>Our facilitators lead short debriefs between climbs, linking what happened on the wall to how your team works back at the office.</p>
        <p>Suited to new teams, merged departments and groups preparing for a big project.</p>
      </div>
    </div>
    <p class="more">Custom Programs<br>For Every Team</p>
    <div class="photo" role="img" aria-label="Illustration of climbers silhouetted helping each other up a hill"></div>
  </article>

  <article class="panel leadership">
    <div class="photo" role="img" aria-label="Photograph of a corporate group gathered outdoors in a forest"></div>
    <div class="band"><h2 class="heading">Leadership Programs</h2></div>
    <div class="content">
      <h3 class="sub">Wilderness Leadership Challenge</h3>
      <div class="body-text">
        <p>A guided day of hiking and challenge initiatives for managers and leadership teams. Each leg of the route puts a different person in charge of decisions.</p>
        <p>Coaching conversations along the trail help leaders see their own style, give honest feedback and plan how to support their teams.</p>
        <p>Every group leaves with a written summary of insights and goals.</p>
      </div>
    </div>
  </article>

  <article class="panel retreat">
    <div class="content">
      <h2 class="heading">Team Retreats</h2>
      <h3 class="sub">Sea to Summit Team Retreat – Vancouver</h3>
      <div class="body-text"><p>Two days on the water and trails of the North Shore, combining adventure, teamwork and facilitated reflection for your whole team.</p></div>
      <h3 class="activities-title">Activities</h3>
      <ul class="activities">
        <li><svg width="7" height="7" viewBox="0 0 10 10" aria-hidden="true"><path d="M1 5l3 3 5-6" stroke="#3f9a2c" stroke-width="2" fill="none"/></svg>Sea Kayaking</li>
        <li><svg width="7" height="7" viewBox="0 0 10 10" aria-hidden="true"><path d="M1 5l3 3 5-6" stroke="#3f9a2c" stroke-width="2" fill="none"/></svg>Rock Climbing</li>
        <li><svg width="7" height="7" viewBox="0 0 10 10" aria-hidden="true"><path d="M1 5l3 3 5-6" stroke="#3f9a2c" stroke-width="2" fill="none"/></svg>Hiking</li>
        <li><svg width="7" height="7" viewBox="0 0 10 10" aria-hidden="true"><path d="M1 5l3 3 5-6" stroke="#3f9a2c" stroke-width="2" fill="none"/></svg>Challenge Initiatives</li>
      </ul>
    </div>
    <div class="dates">
      <div class="label">Book Your Dates</div>
      <div class="date-pills"><span class="pill">May – June</span><span class="pill">July – September</span></div>
    </div>
    <div class="lower" role="img" aria-label="Photograph of a team kayaking on calm water">
      <div class="location">
        <h3 class="activities-title">Location</h3>
        <p class="body-text">Parks and waterways of the North Shore, minutes from downtown</p>
      </div>
      <div class="price"><span class="amount">$95</span><span class="per">Per<br>Participant</span></div>
    </div>
  </article>
</section>

</body>
</html>
```